Business Card Design

Selling beds and mattrices
See website www.lunorest.com.au for details
Targeting wholesale bed sellers

Industry/Entity Type

Business

Contact Information for Business Card

Lunorest
Director Gerald Whitcombe
Beds and Mattrices - Most technologically advanced beds in the world
European designed and made
Already No 1 seller in Europe
Call now for a quote
ph: 0472 518 306
Email: sales@lunorest.com.au
www.lunorest.com.au

```html
<!DOCTYPE html>
<html lang="en">
<head>
<meta charset="utf-8">
<title>Lunorest Business Card</title>
<link rel="stylesheet" href="https://fonts.googleapis.com/css2?family=Lato:wght@400;700;900&display=swap">
<style>
  :root {
    --backdrop: #2b2b2d;
    --card: #ffffff;
    --ink: #161616;
    --accent: #6672a8;
    --muted: #555a60;
    --pill-text: #ffffff;
  }
  * { margin: 0; padding: 0; box-sizing: border-box; }
  html, body { width: 1200px; height: 900px; overflow: hidden; }
  body {
    background: var(--backdrop);
    font-family: "Lato", Arial, sans-serif;
    position: relative;
  }
  .card {
    position: absolute;
    left: 100px; top: 165px;
    width: 1000px; height: 570px;
    background: var(--card);
    border-radius: 44px;
    color: var(--ink);
  }
  .brand {
    position: absolute; left: 62px; top: 178px;
    display: flex; align-items: center; gap: 16px;
  }
  .brand-mark { width: 34px; height: 34px; background: var(--ink); }
  .brand-name {
    font-size: 52px; font-weight: 400; letter-spacing: 2px;
    text-transform: uppercase; color: var(--ink); line-height: 1;
  }
  .rule { position: absolute; height: 3px; background: var(--ink); }
  .rule-top { left: 340px; top: 150px; width: 600px; }
  .rule-brand { left: 62px; top: 262px; width: 360px; }
  .person { position: absolute; right: 60px; top: 92px; text-align: right; }
  .person-name {
    font-size: 36px; font-weight: 900; color: var(--accent);
    text-transform: uppercase; letter-spacing: 0.5px; line-height: 1;
  }
  .person-role {
    margin-top: 22px; font-size: 22px; color: var(--muted);
    text-transform: uppercase; letter-spacing: 1px;
  }
  .pill {
    position: absolute; right: 60px; top: 220px;
    background: var(--accent); color: var(--pill-text);
    border-radius: 28px; padding: 12px 30px;
    font-size: 25px; font-weight: 700; text-transform: uppercase; letter-spacing: 0.5px;
  }
  .quote { position: absolute; left: 62px; top: 292px; }
  .quote-label {
    font-size: 25px; font-weight: 700; color: var(--accent);
    text-transform: uppercase; letter-spacing: 0.5px;
  }
  .quote-phone { font-size: 44px; font-weight: 700; line-height: 1.1; }
  .tagline {
    position: absolute; left: 62px; top: 392px;
    font-size: 27px; font-weight: 900; text-transform: uppercase;
    line-height: 1.35; letter-spacing: 0.3px;
  }
  .contact {
    position: absolute; display: flex; align-items: center; gap: 16px;
    font-size: 26px; font-weight: 400;
  }
  .contact svg { flex: none; }
  .contact-email { right: 60px; top: 375px; }
  .contact-web { left: 62px; top: 495px; font-size: 30px; }
</style>
</head>
<body>
  <main class="card">
    <div class="rule rule-top"></div>
    <div class="person">
      <div class="person-name">Gerald Whitcombe</div>
      <div class="person-role">Director</div>
    </div>

    <div class="brand">
      <span class="brand-mark"></span>
      <span class="brand-name">Lunorest</span>
    </div>
    <div class="rule rule-brand"></div>

    <div class="pill">Continental Beds &amp; Furniture</div>

    <div class="quote">
      <div class="quote-label">Get a quote today</div>
      <div class="quote-phone">0472 518 306</div>
    </div>

    <p class="tagline">Latest technologically advanced<br>European designed &amp; most comfortable matresses</p>

    <div class="contact contact-email">
      <svg width="44" height="30" viewBox="0 0 44 30" aria-hidden="true">
        <rect x="1" y="1" width="42" height="28" fill="var(--accent)"/>
        <path d="M2 2 L22 18 L42 2" fill="none" stroke="#fff" stroke-width="2.5"/>
        <path d="M2 28 L17 14 M42 28 L27 14" fill="none" stroke="#fff" stroke-width="2"/>
      </svg>
      <span>sales@lunorest.com.au</span>
    </div>

    <div class="contact contact-web">
      <svg width="38" height="38" viewBox="0 0 38 38" aria-hidden="true">
        <circle cx="19" cy="19" r="18" fill="var(--accent)"/>
        <ellipse cx="19" cy="19" rx="8" ry="17" fill="none" stroke="#fff" stroke-width="2"/>
        <path d="M2 19 H36 M5 10 H33 M5 28 H33" stroke="#fff" stroke-width="2"/>
      </svg>
      <span>www.lunorest.com.au</span>
    </div>
  </main>
</body>
</html>
```